K&T Fixit and Rebuild general contracting business card design

I already have a logo that I want to use and I need a card that uses that logo and color scheme on the front with the address phone numbers and email and on the back a place for technicians to write in their name and phone number when they hand it out. It will need the License number of License #KTFXTRB318QN.
It should say General Contractor under the company name. The address is
4417 NE 3rd Ave, Ste D246
Vancouver, WA 98612
www.kandtfixitandrebuild.example
office@kandtfixitandrebuild.example
360-555-0182 is the telephone number
360-555-0149 is the fax number

Target Market(s)

Homeowners needing remodel work or repairs in their home.

Industry/Entity Type

Construction

Contact Information for Business Card

Business name, address, phone number, license number, fax number, email, and website on the front and a place to fill in technician's name and number

Font styles to use
Serif

Requirements
Must have
• Business name, address, phone number, license number, fax number, email, and website on the front and a place to fill in technician's name and number
Nice to have
• I uploaded an example of a front that is good.
Should not have
• Froo froo or extra embellishments.

```html
<!DOCTYPE html>
<html lang="en">
<head>
<meta charset="utf-8">
<title>K&amp;T Fixit and Rebuild – Business Card</title>
<link href="https://fonts.googleapis.com/css2?family=Roboto+Slab:wght@500;700&family=Source+Serif+4:wght@400;600&display=swap" rel="stylesheet">
<style>
  :root {
    --page-bg: #2b2b2b;
    --wood-light: #d99a4e;
    --wood-mid: #c47f33;
    --wood-deep: #a8621f;
    --ink-brown: #7e3a0d;
    --slate-light: #4a4a4a;
    --slate-dark: #2e2e2e;
    --band: #353535;
    --ink-dark: #1f1a16;
    --white: #f4f4f4;
    --muted: #bdbdbd;
    --accent-orange: #d8862f;
    --display: "Roboto Slab", Georgia, serif;
    --text: "Source Serif 4", Georgia, serif;
  }
  * { margin: 0; padding: 0; box-sizing: border-box; }
  html, body { width: 1200px; height: 1138px; overflow: hidden; }
  body {
    background: var(--page-bg);
    font-family: var(--text);
    position: relative;
  }
  .card {
    position: absolute;
    left: 274px;
    width: 622px;
    height: 375px;
    border-radius: 14px;
    overflow: hidden;
    box-shadow: 0 4px 10px rgba(0,0,0,0.45);
  }
  .card--front { top: 186px; }
  .card--back { top: 608px; }

  .wood-surface {
    position: absolute; inset: 0;
    background: linear-gradient(100deg, var(--wood-mid) 0%, var(--wood-light) 45%, var(--wood-mid) 75%, var(--wood-deep) 100%);
  }
  .slate-surface {
    position: absolute; inset: 0;
    background: linear-gradient(160deg, var(--slate-light) 0%, var(--slate-dark) 60%, #3a3a3a 100%);
  }

  /* Front */
  .front-brand {
    position: absolute;
    top: 96px; left: 0; right: 0;
    text-align: center;
    color: var(--ink-brown);
  }
  .front-brand-name {
    font-family: var(--display);
    font-weight: 700;
    font-size: 44px;
    line-height: 52px;
    white-space: nowrap;
  }
  .front-brand-role {
    font-family: var(--display);
    font-weight: 500;
    font-size: 20px;
    letter-spacing: 4px;
    text-transform: uppercase;
    margin-top: 8px;
  }
  .front-band {
    position: absolute;
    top: 284px; left: 0; right: 0; height: 38px;
    background: var(--band);
    color: var(--white);
    font-size: 17px;
    line-height: 38px;
    text-align: center;
  }
  .front-footer {
    position: absolute;
    top: 333px; left: 0; right: 0;
    text-align: center;
    font-size: 16px;
    color: var(--ink-dark);
    white-space: nowrap;
  }
  .front-footer .divider { margin: 0 18px; }

  /* Back */
  .back-brand {
    position: absolute;
    top: 58px; left: 24px; width: 270px;
    text-align: center;
    color: var(--white);
  }
  .back-brand-name {
    font-family: var(--display);
    font-weight: 700;
    font-size: 36px;
    line-height: 40px;
  }
  .back-brand-role {
    font-family: var(--display);
    font-weight: 500;
    font-size: 15px;
    letter-spacing: 3px;
    text-transform: uppercase;
    margin-top: 8px;
  }
  .back-license {
    position: absolute;
    top: 196px; left: 59px; width: 200px;
    text-align: center;
    font-size: 16px;
    line-height: 22px;
    color: var(--white);
  }

  .write-in {
    position: absolute;
    top: 34px; right: 22px; width: 260px;
    color: var(--white);
  }
  .write-in-field { margin-bottom: 14px; }
  .write-in-line {
    height: 26px;
    border-bottom: 1.5px solid var(--accent-orange);
  }
  .write-in-label {
    font-size: 12px;
    letter-spacing: 1px;
    text-transform: uppercase;
    color: var(--muted);
    text-align: right;
    margin-top: 3px;
  }
  .address {
    position: absolute;
    top: 150px; right: 22px;
    text-align: right;
    font-size: 16px;
    line-height: 23px;
    color: var(--white);
  }

  .wave { position: absolute; left: 0; top: 0; width: 622px; height: 375px; }

  .contact-list {
    position: absolute;
    top: 262px; right: 22px;
    list-style: none;
    color: var(--ink-dark);
    font-size: 16px;
  }
  .contact-list li {
    height: 23.5px;
    display: flex;
    justify-content: flex-end;
    align-items: center;
    gap: 10px;
    white-space: nowrap;
  }
  .contact-list svg { width: 14px; height: 14px; fill: var(--ink-dark); flex: none; }
</style>
</head>
<body>

<section class="card card--front" aria-label="Business card front">
  <div class="wood-surface" role="img" aria-label="Warm wood grain texture"></div>
  <div class="front-brand">
    <p class="front-brand-name">K&amp;T Fixit and Rebuild</p>
    <p class="front-brand-role">General Contractor</p>
  </div>
  <div class="front-band">Home Maintenance &amp; Remodeling Contractors</div>
  <p class="front-footer">License #KTFXTRB318QN<span class="divider">|</span>www.kandtfixitandrebuild.example</p>
</section>

<section class="card card--back" aria-label="Business card back">
  <div class="slate-surface" role="img" aria-label="Dark grey wood grain texture"></div>

  <svg class="wave" viewBox="0 0 622 375" aria-hidden="true">
    <path d="M0,292 C140,318 280,310 380,262 C470,218 560,204 622,206 L622,375 L0,375 Z" fill="var(--wood-mid)"/>
    <path d="M0,318 C150,340 290,320 390,280 C470,246 560,224 622,222" fill="none" stroke="var(--slate-dark)" stroke-width="8"/>
    <path d="M40,302 C170,320 280,312 370,282" fill="none" stroke="var(--slate-dark)" stroke-width="3"/>
  </svg>

  <div class="back-brand">
    <p class="back-brand-name">K&amp;T Fixit<br>and Rebuild</p>
    <p class="back-brand-role">General Contractor</p>
  </div>
  <p class="back-license">License No.:<br>#KTFXTRB318QN</p>

  <div class="write-in" aria-label="Space for technician details">
    <div class="write-in-field">
      <div class="write-in-line"></div>
      <p class="write-in-label">Technician</p>
    </div>
    <div class="write-in-field">
      <div class="write-in-line"></div>
      <p class="write-in-label">Direct Phone</p>
    </div>
  </div>

  <p class="address">4417 NE 3rd Ave, Ste D246<br>Vancouver, WA 98612</p>

  <ul class="contact-list">
    <li>360-555-0182
      <svg viewBox="0 0 16 16"><path d="M2 6c0-2 2-3 6-3s6 1 6 3v1h-3V5.5H5V7H2z M4 8h8l2 5H2z"/></svg>
    </li>
    <li>360-555-0149
      <svg viewBox="0 0 16 16"><path d="M4 1h8v4H4z M1 6h14v6h-3v3H4v-3H1z M5 10v4h6v-4z" fill-rule="evenodd"/></svg>
    </li>
    <li>kandtfixitandrebuild.example
      <svg viewBox="0 0 16 16"><circle cx="8" cy="8" r="6.5" fill="none" stroke="var(--ink-dark)" stroke-width="1.5"/><path d="M1.5 8h13M8 1.5v13" stroke="var(--ink-dark)" stroke-width="1.2"/><ellipse cx="8" cy="8" rx="3" ry="6.5" fill="none" stroke="var(--ink-dark)" stroke-width="1.2"/></svg>
    </li>
    <li>office@kandtfixitandrebuild.example
      <svg viewBox="0 0 16 16"><path d="M1 3h14v10H1z M2 4.5v.5l6 4 6-4v-.5z" fill-rule="evenodd"/></svg>
    </li>
  </ul>
</section>

</body>
</html>
```